Landcape Construction Company needs a flyer to catch attention

A flyer that can be displayed at several different stores detailing our skills, work produced, experience and contact details. Information can be extracted from our website www.brvkw.co.nz. The flyer should feel very green, with addition of pics of work completed as well as stock images of lush green plants, lawns, landscape or similar. Needs to be eye catching with just enough information to express our experience and commitment to high standards

Target Market(s)

Residential
Landscape Architects

Industry/Entity Type

Landscaping

Font styles to use
Serif

Colors
abd037

Requirements
Must have
• Our logo
Experience
Services offered including pictures
All information avail on our website www.brvkw.co.nz
Nice to have
• stock images of lush greenery like a garden after fresh rainfall
Should not have
• Nothing comes to mind

```html
<!DOCTYPE html>
<html lang="en">
<head>
<meta charset="utf-8">
<title>Greenvale Build Company – Flyer</title>
<link rel="stylesheet" href="https://fonts.googleapis.com/css2?family=EB+Garamond:wght@500;600&family=Source+Sans+3:wght@400;600;700&display=swap">
<style>
  :root {
    --brand-green: #a3c45f;
    --brand-green-bright: #abd037;
    --deep-green: #2e7a45;
    --leaf-dark: #1f3322;
    --leaf-mid: #4f7a44;
    --text-dark: #1c1c1c;
    --text-grey: #4a4a4a;
    --white: #ffffff;
    --rule-grey: #d6d6d6;
  }
  * { box-sizing: border-box; margin: 0; padding: 0; }
  html, body { width: 1200px; height: 1103px; overflow: hidden; background: var(--white); }
  .canvas { position: relative; width: 1200px; height: 1103px; background: var(--white); font-family: "Source Sans 3", sans-serif; }

  /* Left panel */
  .cover { position: absolute; left: 87px; top: 58px; width: 523px; height: 1007px; }
  .cover__foliage { position: absolute; left: 0; top: 0; width: 523px; height: 720px;
    background: radial-gradient(ellipse at 30% 30%, #5e8a4e 0%, var(--leaf-mid) 30%, #2f4a2c 65%, var(--leaf-dark) 100%); }
  .cover__card { position: absolute; left: 83px; top: 84px; width: 358px; height: 601px; background: var(--white); border-top: 8px solid var(--brand-green); }
  .brand { position: absolute; top: 44px; left: 0; width: 100%; text-align: center; }
  .brand__mark { display: block; margin: 0 auto; }
  .brand__name { margin-top: 6px; color: var(--deep-green); font-weight: 600; font-size: 14px; line-height: 15px; letter-spacing: -0.2px; }
  .cover__intro { position: absolute; top: 202px; left: 0; width: 100%; text-align: center;
    font-family: "EB Garamond", serif; font-weight: 600; font-size: 22px; line-height: 35.4px; letter-spacing: 1.3px; color: var(--text-dark); }
  .cover__web { position: absolute; left: 0; top: 720px; width: 523px; height: 96px; background: var(--brand-green);
    display: flex; align-items: center; justify-content: center; color: var(--white); font-weight: 700; font-size: 22px; letter-spacing: 2.6px; }
  .cover__garden { position: absolute; left: 0; top: 816px; width: 523px; height: 191px;
    background: linear-gradient(120deg, #c9b08a 0%, #8d8a5a 35%, #3d5a33 60%, #b99a72 100%); }

  /* Right panel */
  .services-panel { position: absolute; left: 628px; top: 58px; width: 525px; height: 1007px; border-left: 1px solid var(--rule-grey); border-right: 1px solid var(--rule-grey); }
  .services-panel__band { position: absolute; left: -1px; top: 0; width: 526px; height: 37px; background: var(--brand-green); }
  .work-photo { position: absolute; }
  .work-photo--path { left: 43px; top: 25px; width: 207px; height: 155px; background: linear-gradient(160deg, #8a5a44 0%, #6d9a48 40%, #b9b7ae 60%, #2b2b22 100%); }
  .work-photo--fence { left: 262px; top: 23px; width: 209px; height: 157px; background: linear-gradient(100deg, #8b4a26 0%, #a9643a 55%, #c6c9cc 85%, #9a9ea2 100%); }
  .service-icons { position: absolute; left: 0; top: 232px; width: 100%; height: 54px; }
  .services__title { position: absolute; top: 321px; left: 0; width: 100%; text-align: center; color: var(--brand-green);
    font-weight: 700; font-size: 33px; letter-spacing: 4px; line-height: 1; padding-left: 4px; }
  .services__list { position: absolute; top: 0; left: 0; width: 100%; list-style: none; font-size: 16.8px; line-height: 18px; color: var(--text-grey); letter-spacing: 0.2px; }
  .services__list li { position: absolute; white-space: nowrap; transform: translateX(-50%); }
  .work-photo--pool { left: -1px; top: 557px; width: 526px; height: 187px; background: linear-gradient(180deg, #3e5136 0%, #55684a 30%, #c8c9c5 45%, #7fa0a2 65%, #d3d3d0 100%); }
  .work-photo--deck { left: -1px; top: 750px; width: 526px; height: 188px; background: linear-gradient(180deg, #4f6a39 0%, #5f7d42 60%, #8a7565 78%, #6e5b4e 100%); }
  .services-panel__contact { position: absolute; left: -1px; top: 938px; width: 526px; height: 69px; background: var(--brand-green);
    color: var(--white); font-weight: 700; font-size: 15px; letter-spacing: 1.6px; }
  .contact-item { position: absolute; top: 26px; display: flex; align-items: center; gap: 7px; }
  .contact-item--phone { left: 111px; top: 23px; }
  .contact-item--email { left: 268px; }
</style>
</head>
<body>
<div class="canvas">

  <section class="cover">
    <div class="cover__foliage" role="img" aria-label="Lush tropical foliage with monstera, palm and banana leaves"></div>
    <div class="cover__card">
      <div class="brand">
        <svg class="brand__mark" width="90" height="90" viewBox="0 0 90 90" aria-hidden="true">
          <circle cx="45" cy="45" r="44" fill="var(--brand-green)"/>
        </svg>
        <div class="brand__name">Greenvale Build<br>Company Ltd</div>
      </div>
      <p class="cover__intro">More than 25 years<br>experience in the<br>landscaping industry,<br>we offer services<br>to large or small<br>residential and<br>commercial projects</p>
    </div>
    <div class="cover__web">www.brvkw.co.nz</div>
    <div class="cover__garden" role="img" aria-label="Aerial view of a planted garden with gravel beds, palms and white flowering shrubs"></div>
  </section>

  <section class="services-panel">
    <div class="services-panel__band"></div>
    <div class="work-photo work-photo--path" role="img" aria-label="Completed concrete path beside fresh lawn and brick seating wall"></div>
    <div class="work-photo work-photo--fence" role="img" aria-label="Completed horizontal timber slat fence"></div>

    <svg class="service-icons" viewBox="0 0 525 54" aria-hidden="true" fill="none" stroke="var(--deep-green)" stroke-width="1.6" stroke-linecap="round" stroke-linejoin="round">
      <g><circle cx="148" cy="27" r="26"/><circle cx="148" cy="27" r="23" stroke="var(--brand-green)"/>
        <path d="M136 37 h8 l10 -4 M140 34 h10"/><path d="M151 31 c-2 -8 2 -14 8 -16 c1 7 -2 13 -8 16z"/></g>
      <g><circle cx="223" cy="27" r="26"/><circle cx="223" cy="27" r="23" stroke="var(--brand-green)"/>
        <path d="M223 38 v-12 M217 26 h12 M219 38 h8 M212 20 l-3 -2 M234 20 l3 -2 M214 24 l-4 0 M232 24 l4 0"/></g>
      <g><circle cx="297" cy="27" r="26"/><circle cx="297" cy="27" r="23" stroke="var(--brand-green)"/>
        <path d="M285 21 l2 -4 l2 4 v16 h-4z M293 21 l2 -4 l2 4 v16 h-4z M301 21 l2 -4 l2 4 v16 h-4z M285 25 h20 M285 32 h20"/></g>
      <g><circle cx="372" cy="27" r="26"/><circle cx="372" cy="27" r="23" stroke="var(--brand-green)"/>
        <path d="M366 38 v-8 M366 30 c-6 0 -7 -10 0 -14 c7 4 6 14 0 14z M378 38 v-6 M378 32 c-5 0 -6 -8 0 -11 c6 3 5 11 0 11z M360 38 h24"/></g>
    </svg>

    <h2 class="services__title">SERVICES</h2>
    <ul class="services__list">
      <li style="left:97px;top:384px">FENCING</li>
      <li style="left:238px;top:384px">PATIOS</li>
      <li style="left:408px;top:384px">RETAINING WALLS</li>
      <li style="left:97px;top:416px">BOARDWALKS</li>
      <li style="left:238px;top:416px">PAVING</li>
      <li style="left:408px;top:416px">GARDENS &amp; LAWNS</li>
      <li style="left:97px;top:448px">TIMBER</li>
      <li style="left:238px;top:448px">CONCRETE</li>
      <li style="left:408px;top:448px">IRRIGATION</li>
      <li style="left:97px;top:480px">PLANTER BOXES</li>
      <li style="left:238px;top:480px">WATER FEATURES</li>
      <li style="left:408px;top:480px">PROJECT MANAGEMENT</li>
      <li style="left:97px;top:511px">PERGOLAS</li>
      <li style="left:238px;top:511px">DECKING</li>
      <li style="left:408px;top:511px">CONSULTATION</li>
    </ul>

    <div class="work-photo work-photo--pool" role="img" aria-label="Swimming pool with stone paving and timber decking, framed by hedges"></div>
    <div class="work-photo work-photo--deck" role="img" aria-label="Timber deck with lounge chair in front of a green hedge wall"></div>

    <div class="services-panel__contact">
      <div class="contact-item contact-item--phone">
        <svg width="15" height="26" viewBox="0 0 15 26" aria-hidden="true"><rect x="1" y="1" width="13" height="24" rx="2" fill="none" stroke="var(--white)" stroke-width="2"/><rect x="3" y="4" width="9" height="15" fill="var(--white)"/><circle cx="7.5" cy="22" r="1.2" fill="var(--white)"/></svg>
        <span>021 555 0142</span>
      </div>
      <div class="contact-item contact-item--email">
        <svg width="22" height="16" viewBox="0 0 22 16" aria-hidden="true" fill="none" stroke="var(--white)" stroke-width="1.6"><rect x="1" y="1" width="20" height="14"/><path d="M1 1 l10 8 l10 -8 M1 15 l7 -7 M21 15 l-7 -7"/></svg>
        <span>info@brvkw.co.nz</span>
      </div>
    </div>
  </section>

</div>
</body>
</html>
```